vQ CARELINE (Brochure Design)

i need a proffesional brochure made. we are a mobile medical service company providing mobile Arterial Blood Gases(ABG's). Respiratory & Ventilator Consultation services. Ventilator and Tracheostomy training courses. and mobile vaccine administration.

this is my first time making a brochure so any and all advice/guidance will be appreciated.

i am thinking prints will be 8.5 inches x 11 inches (TRI-FOLD and BI-FOLD)

i have uploaded my business card design and logo design for reference.
as this brochure project continues ill update needs of the project descriptions.

Introduction: At vq CARELINE, we're dedicated to enhancing healthcare services by providing exceptional mobile arterial blood gases, respiratory and ventilator consultation services. Our core values revolve around excellence, compassion and accessibility. We believe that every individual deserves the highest standard of care, and we're committed to delivering that through expert guidance and top-notch training courses. Your health is at the heart of what we do, and we're here to support you on your journey to better respiratory health.

Mobile Arterial Blood Gases : Our mobile Arterial Blood Gas service offers quick, on-the-spot analysis of pH, oxygen, and carbon dioxide levels in your the blood. This service enables rapid adjustments to treatment plans for more effective respiratory care.

Ventilator and Tracheostomy Training: Our ventilator and tracheostomy course empowers caregivers and healthcare professionals to manage ventilators and care for tracheostomy patients with expertise. This training enhances patient safety, treatment outcomes, and healthcare provider confidence. vQ Careline your choice for top-notch care, convenience, and peace of mind.

Respiratory Consulting: Our respiratory consulting services provide expert guidance and support for individuals with respiratory / ventilator concerns. Benefits include personalized treatment plans, better management of respiratory conditions, and improved overall lung health. vQ Careline is your trusted partner for a breath of fresh air.

Target Market(s)

Sub-Acute facilities, Pulmonary Clinics, Pulmonologists, Nurses, Caregivers, Hospice and homehealth companies.

Industry/Entity Type

Medical; Respiratory; Nursing

Requirements
Must have
• proffesional simple design.

```html
<!DOCTYPE html>
<html lang="en">
<head>
<meta charset="utf-8">
<title>vQ CARELINE – Tri-fold Brochure</title>
<link rel="stylesheet" href="https://fonts.googleapis.com/css2?family=Poppins:wght@400;500;600;700;800&display=swap">
<style>
:root{
  --blue:#3a8fd6;
  --blue-deep:#2367b8;
  --green:#3cc55c;
  --green-soft:#5bd67a;
  --ink:#1d1d1f;
  --body:#3a3a3c;
  --paper:#ffffff;
  --paper-grey:#f1f1f1;
  --bg:#e9e7e3;
}
*{box-sizing:border-box;margin:0;padding:0}
html,body{width:1200px;height:1095px;overflow:hidden;background:var(--bg);font-family:"Poppins",sans-serif;color:var(--body)}
.spread{position:absolute;left:257px;width:686px;height:530px;display:flex;box-shadow:0 4px 18px rgba(0,0,0,.18)}
.spread--outside{top:12px}
.spread--inside{top:553px}
.panel{position:relative;width:228.67px;height:100%;background:var(--paper);overflow:hidden}
.panel + .panel{border-left:1px solid #e2e2e2}
.abs{position:absolute}
.stripes{position:absolute;left:0;top:0}
.body-copy{font-size:7.6px;line-height:1.42;color:var(--body)}
.body-copy p+p{margin-top:8px}
.lead{font-weight:600;color:var(--ink)}

/* outside */
.intro-title{left:30px;top:30px;font-size:15.5px;font-weight:600;letter-spacing:.5px;line-height:1.75}
.intro-title .t1{color:var(--blue)} .intro-title .t2{color:var(--green)}
.intro-copy{left:20px;top:104px;width:196px}
.values{left:14px;top:382px;font-size:15px;font-weight:600;letter-spacing:.6px;line-height:1.75}
.values span{display:block}
.values .v1{color:var(--green)} .values .v2{color:var(--blue);padding-left:16px} .values .v3{color:var(--green);padding-left:52px}

.panel--partner{background:var(--blue)}
.partner-head{left:0;top:8px;width:100%;text-align:center;font-weight:800;line-height:1.18}
.partner-head .w{color:#fff;font-size:25px;display:block}
.partner-head .g{color:var(--green);font-size:16px;display:block;font-weight:700}
.brand{display:flex;align-items:center;gap:6px;font-weight:500;font-size:13px;letter-spacing:.3px;white-space:nowrap}
.brand i{display:block;width:16px;height:16px}
.brand--light{color:#fff}.brand--light i{background:#fff}
.brand--dark{color:var(--ink)}.brand--dark i{background:var(--blue)}
.partner-brand{left:0;width:100%;top:246px;justify-content:center}
.call{left:0;width:100%;top:316px;text-align:center;color:#fff}
.call .c1{font-size:19px;font-weight:400;display:block}
.call .c2{font-size:16px;font-weight:600;letter-spacing:1.6px;display:block;margin-top:-2px}
.contact-box{left:20px;top:400px;width:188px;height:130px;background:var(--paper);text-align:center;padding-top:14px}
.contact-box h3{color:var(--green);font-size:11.5px;font-weight:700;letter-spacing:.4px}
.contact-box hr{border:0;border-top:1px solid var(--green);width:70px;margin:6px auto 9px}
.contact-box p{font-size:7px;color:var(--ink);line-height:2.2}

.panel--cover{background:var(--paper-grey)}
.device-shot{left:10px;top:22px;width:205px;height:200px;border-radius:10px;background:linear-gradient(160deg,#d8ddf0 0%,#9fb4de 55%,#8a7fc9 100%);opacity:.92}
.cover-brand{left:30px;top:268px}
.cover-head{left:22px;top:312px;font-size:21px;font-weight:700;line-height:1.24;letter-spacing:.3px}
.cover-head span{display:block}
.cover-head .b{color:var(--blue)} .cover-head .k{color:var(--ink)} .cover-head .g{color:var(--green)}
.cover-web{left:0;width:100%;top:494px;text-align:center;font-size:8px;color:var(--ink)}

/* inside */
.svc-head{left:18px;top:20px;font-size:17.5px;font-weight:700;line-height:1.2;letter-spacing:.3px}
.svc-head span{display:block}
.svc-head .k{color:var(--ink)} .svc-head .g{color:var(--green)}
.svc-copy{left:14px;width:200px}
.tagline{font-size:10px;font-weight:600;color:var(--green);letter-spacing:.5px;line-height:1.3}
.abg-photo{left:0;top:206px;width:210px;height:92px;background:linear-gradient(120deg,#e6ecf2 0%,#c9b7a8 55%,#a9c0d8 100%)}
.abg-rule{left:0;top:198px;width:218px;height:5px;background:var(--blue-deep)}
.abg-title{left:0;width:100%;top:314px;text-align:center;font-size:8.6px;font-weight:500;color:var(--ink)}
.abg-table{left:28px;top:337px;border-collapse:collapse;font-size:7.2px;color:var(--ink)}
.abg-table th,.abg-table td{border:1px solid #777;padding:2.5px 5px;text-align:center;font-weight:400}
.abg-table th{font-weight:600}
.abg-table td:first-child{text-align:left}
.artery-art{left:150px;top:348px;width:64px;height:168px;border-radius:30px 30px 8px 8px;background:linear-gradient(180deg,#f1d6d2 0%,#d98a86 60%,#c65a57 100%)}
.artery-label{left:150px;top:336px;font-size:6.5px;color:var(--ink)}

.train-frame{left:8px;top:242px;width:212px;height:108px;background:var(--green);padding:4px}
.train-photo{width:100%;height:100%;background:linear-gradient(110deg,#7d6aa8 0%,#c9c3d6 45%,#8ea0c4 100%)}
.step{left:30px;width:174px;height:36px;background:var(--green);display:flex;align-items:center;gap:8px;padding:0 8px;color:#fff}
.step b{font-size:15px;font-weight:400;opacity:.85}
.step span{font-size:6.1px;line-height:1.3}

.consult-frame{left:0;top:244px;width:228.67px;height:286px;background:var(--blue-deep);padding:8px 0 8px 8px}
.consult-photo{width:100%;height:100%;background:linear-gradient(135deg,#cfc6bb 0%,#8aa6c9 50%,#e7e4e0 100%)}
</style>
</head>
<body>

<!-- Outside of the tri-fold -->
<section class="spread spread--outside">
  <article class="panel panel--intro">
    <h2 class="abs intro-title"><span class="t1">WHO WE ARE</span><br><span class="t2">WHAT WE DO</span></h2>
    <div class="abs intro-copy body-copy">
      <p class="lead">At vQ CARELINE, we’re dedicated to enhancing healthcare services by providing exceptional mobile arterial blood gases, respiratory and ventilator consultation services.</p>
      <p>Our core values revolve around excellence, compassion and accessibility. We believe that every individual deserves the highest standard of care, and we’re committed to delivering that through expert guidance and top-notch training courses.</p>
      <p>Your health is at the heart of what we do, and we’re here to support you on your journey to better respiratory health.</p>
    </div>
    <svg class="stripes" width="229" height="530" aria-hidden="true">
      <polygon points="80,312 118,312 229,432 229,472" fill="var(--green)"/>
      <polygon points="135,312 170,312 229,375 229,412" fill="var(--green-soft)"/>
    </svg>
    <p class="abs values"><span class="v1">Excellence</span><span class="v2">Compassion</span><span class="v3">Accessibility</span></p>
  </article>

  <article class="panel panel--partner">
    <svg class="stripes" width="229" height="530" aria-hidden="true">
      <polygon points="150,0 200,0 229,32 229,88" fill="var(--paper)" opacity=".9"/>
      <polygon points="200,0 229,0 229,32" fill="var(--green-soft)"/>
    </svg>
    <h1 class="abs partner-head">
      <span class="w">YOUR</span><span class="g">PARTNER FOR</span>
      <span class="w">BETTER</span><span class="g">RESPIRATORY</span>
      <span class="w">HEALTH</span>
    </h1>
    <div class="abs brand brand--light partner-brand"><i></i>vQ CARELINE</div>
    <p class="abs call"><span class="c1">Call us!</span><span class="c2">555.014.2994</span></p>
    <div class="abs contact-box">
      <h3>CONTACT US:</h3>
      <hr>
      <p>Email: info@vqcareline.com<br>Phone: 555.014.2994<br>Fax: 555.014.2223<br>vqcareline.com</p>
    </div>
  </article>

  <article class="panel panel--cover">
    <svg class="stripes" width="229" height="530" aria-hidden="true">
      <polygon points="0,0 30,0 229,210 229,262" fill="var(--green)"/>
      <polygon points="60,0 96,0 229,140 229,178" fill="var(--green-soft)"/>
      <polygon points="0,40 0,90 229,330 229,280" fill="var(--green)" opacity=".0"/>
    </svg>
    <div class="abs device-shot" role="img" aria-label="Photo of two portable ventilator units"></div>
    <div class="abs brand brand--dark cover-brand"><i></i>vQ CARELINE</div>
    <h1 class="abs cover-head">
      <span class="g">YOUR</span><span class="b">MOBILE</span><span class="k">RESPIRATORY</span><span class="b">CARE</span><span class="b">SOLUTION</span>
    </h1>
    <p class="abs cover-web">vqcareline.com</p>
  </article>
</section>

<!-- Inside of the tri-fold -->
<section class="spread spread--inside">
  <article class="panel panel--abg" style="background:var(--paper-grey)">
    <h2 class="abs svc-head"><span class="k">MOBILE</span><span class="g">ARTERIAL</span><span class="k">BLOOD GASES</span></h2>
    <div class="abs svc-copy body-copy" style="top:110px">Our mobile Arterial Blood Gas service offers quick, on-the-spot analysis of pH, oxygen, and carbon dioxide levels in your the blood. This service enables rapid adjustments to treatment plans for more effective respiratory care.</div>
    <p class="abs tagline" style="left:14px;top:172px">Quick and Effective Analysis</p>
    <div class="abs abg-rule"></div>
    <div class="abs abg-photo" role="img" aria-label="Photo of a blood sample being drawn from an arm"></div>
    <p class="abs abg-title">Arterial Blood Gas (ABG)</p>
    <table class="abs abg-table">
      <tr><th>ABG</th><th>Normal range</th></tr>
      <tr><td>O<sub>2</sub>CT</td><td>15-23% per<br>100 mL of blood</td></tr>
      <tr><td>pH</td><td>7.35-7.45</td></tr>
      <tr><td>PaCO<sub>2</sub></td><td>35-45 mmHg</td></tr>
      <tr><td>PaO<sub>2</sub></td><td>80-100 mmHg</td></tr>
      <tr><td>HCO<sub>3</sub></td><td>22-26 mEq/L</td></tr>
      <tr><td>O<sub>2</sub>Sat</td><td>95-100%</td></tr>
    </table>
    <span class="abs artery-label">Artery</span>
    <div class="abs artery-art" role="img" aria-label="Illustration of an arm showing the radial artery"></div>
  </article>

  <article class="panel panel--training">
    <h2 class="abs svc-head"><span class="k">VENTILATOR</span><span class="g">AND</span><span class="k">TRACHEOSTOMY</span><span class="g">TRAINING</span></h2>
    <div class="abs svc-copy body-copy" style="top:132px;left:24px;width:192px">Our ventilator and tracheostomy course empowers caregivers and healthcare professionals to manage ventilators and care for tracheostomy patients with expertise. This training enhances patient safety, treatment outcomes, and healthcare provider confidence. vQ Careline your choice for top-notch care, convenience, and peace of mind.</div>
    <div class="abs train-frame"><div class="train-photo" role="img" aria-label="Photo of a nurse adjusting a ventilator beside a patient in bed"></div></div>
    <div class="abs step" style="top:402px"><b>01</b><span>Learn how to manage ventilators and care for tracheostomy patients with expertise</span></div>
    <div class="abs step" style="top:454px"><b>02</b><span>Enhance patient safety, treatment outcomes, and healthcare provider confidence</span></div>
  </article>

  <article class="panel panel--consult">
    <h2 class="abs svc-head"><span class="k">RESPIRATORY</span><span class="g">CONSULTING</span></h2>
    <div class="abs svc-copy body-copy" style="top:88px;left:18px;width:196px">Our respiratory consulting services provide expert guidance and support for individuals with respiratory / ventilator concerns. Benefits include personalized treatment plans, better management of respiratory conditions, and improved overall lung health. vQ Careline is your trusted partner for a breath of fresh air.</div>
    <p class="abs tagline" style="left:18px;top:176px">Expert Guidance<br>and Support for<br>Better Lung Health</p>
    <div class="abs consult-frame"><div class="consult-photo" role="img" aria-label="Photo of a caregiver sitting with an elderly patient"></div></div>
  </article>
</section>

</body>
</html>
```